Local Flower Farm Needs Business Card Design

I need business cards designed for a flower farm based in Eudora, Kansas.
Business Info:
We are a local cut flower farm located in Eudora, Kansas, founded by Darla Hoffstrom. What started as a passion for agriculture and search for more joy in daily life has blossomed into a small business dedicated to providing the community with beautiful, fresh, and sustainable flowers. We specialize in local, seasonal blooms, ensuring that every petal reflects the care and dedication we pour into our craft. Our mission is to deliver the highest quality flowers directly to our customers through local farmers markets and to florists who share our commitment to sustainability. Join us in celebrating the beauty of nature, one bloom at a time!
Contact Details:
Darla Hoffstrom
Owner
Phone 913-555-0147
Facebook: Lorabelle Quinn Blossoms
Instagram: @LorabelleQuinnBlossoms
Website: LorabelleQuinnBlossoms.example
Target Market(s)
Wholesale to Florists and Direct to Consumer via Farmers Market
Industry/Entity Type
Florist, Farm
Contact Information for Business Card
Name, Contact Info, Logo
Look and feel

```html
<!DOCTYPE html>
<html lang="en">
<head>
<meta charset="utf-8">
<title>Lorabelle Quinn Blossoms — Business Card</title>
<link rel="stylesheet" href="https://fonts.googleapis.com/css2?family=Montserrat:wght@400;500;700&display=swap">
<style>
  :root {
    --backdrop: #ececec;
    --card-white: #f4f4f6;
    --card-teal: #08272f;
    --ink: #111416;
    --emboss: #123a44;
    --emboss-line: #1b4a55;
    --light-text: #ffffff;
  }
  * { box-sizing: border-box; margin: 0; padding: 0; }
  html, body {
    width: 1200px; height: 1200px; overflow: hidden;
    background: var(--backdrop);
    font-family: "Montserrat", sans-serif;
  }
  .canvas { position: relative; width: 1200px; height: 1200px; }
  .card {
    position: absolute; left: 233px; width: 749px; height: 415px;
  }
  .card--front { top: 101px; background: var(--card-white); color: var(--ink); }
  .card--back { top: 667px; background: var(--card-teal); color: var(--light-text); }

  .brand-seal {
    position: absolute; left: 517px; top: 46px; width: 166px; height: 166px;
    border: 1.5px solid var(--ink); border-radius: 50%;
    display: flex; align-items: center; justify-content: center; text-align: center;
  }
  .brand-seal__name {
    font-weight: 500; font-size: 15px; line-height: 1.3; letter-spacing: 0.08em;
    text-transform: uppercase; color: var(--ink);
  }

  .holder { position: absolute; left: 64px; top: 200px; }
  .holder__name { font-weight: 700; font-size: 25px; line-height: 1.1; }
  .holder__role { font-weight: 400; font-size: 18px; margin-top: 3px; }

  .contact-list { position: absolute; left: 64px; top: 284px; list-style: none; }
  .contact-list__item {
    display: flex; align-items: center; height: 27px;
    font-size: 19.5px; font-weight: 400;
  }
  .contact-list__icon { width: 16px; height: 16px; margin-right: 9px; flex: none; fill: var(--ink); }

  .emboss-seal {
    position: absolute; left: 275px; top: 108px; width: 202px; height: 202px;
    border: 2px solid var(--emboss-line); border-radius: 50%;
    display: flex; align-items: center; justify-content: center; text-align: center;
  }
  .emboss-seal__name {
    font-weight: 500; font-size: 18px; line-height: 1.3; letter-spacing: 0.08em;
    text-transform: uppercase; color: var(--emboss);
  }

  .social-handle {
    position: absolute; left: 54px; top: 349px;
    font-size: 19.5px; font-weight: 400; letter-spacing: 0.02em;
  }
</style>
</head>
<body>
<main class="canvas">
  <section class="card card--front">
    <div class="brand-seal">
      <span class="brand-seal__name">Lorabelle<br>Quinn<br>Blossoms</span>
    </div>

    <div class="holder">
      <h1 class="holder__name">Darla Hoffstrom</h1>
      <p class="holder__role">Owner</p>
    </div>

    <ul class="contact-list">
      <li class="contact-list__item">
        <svg class="contact-list__icon" viewBox="0 0 24 24" aria-hidden="true"><path d="M6.6 10.8a15.1 15.1 0 0 0 6.6 6.6l2.2-2.2c.3-.3.7-.4 1-.2 1.1.4 2.3.6 3.6.6.6 0 1 .4 1 1V20c0 .6-.4 1-1 1A17 17 0 0 1 3 4c0-.6.4-1 1-1h3.5c.6 0 1 .4 1 1 0 1.3.2 2.5.6 3.6.1.3 0 .7-.2 1z"/></svg>
        913-555-0147
      </li>
      <li class="contact-list__item">
        <svg class="contact-list__icon" viewBox="0 0 24 24" aria-hidden="true"><path d="M2 5h20v2l-10 6L2 7z"/><path d="M2 9l10 6 10-6v10H2z"/></svg>
        darla@lorabellequinnblossoms.example
      </li>
      <li class="contact-list__item">
        <svg class="contact-list__icon" viewBox="0 0 24 24" aria-hidden="true"><circle cx="12" cy="12" r="10"/><path d="M12 2a15 15 0 0 1 0 20M12 2a15 15 0 0 0 0 20M2 12h20" stroke="#f4f4f6" stroke-width="1.4" fill="none"/></svg>
        www.lorabellequinnblossoms.example
      </li>
    </ul>
  </section>

  <section class="card card--back">
    <div class="emboss-seal">
      <span class="emboss-seal__name">Lorabelle<br>Quinn<br>Blossoms</span>
    </div>
    <p class="social-handle">@LorabelleQuinnBlossoms</p>
  </section>
</main>
</body>
</html>
```